Diagram for consulting firm website

My consulting firm, Tamsworth Consulting, www.tamsworthconsulting-example.com.au, requires a visual diagram in the style and colours of our website to promote "Restructuring services." Please see the two attached files for content and guidance.

```html
<!DOCTYPE html>
<html lang="en">
<head>
<meta charset="UTF-8">
<title>Types of Corporate Restructuring</title>
<link href="https://fonts.googleapis.com/css2?family=Roboto:wght@400;500;700&display=swap" rel="stylesheet">
<style>
  :root {
    --orange: #F7941D;
    --sky: #29A8E0;
    --royal: #3B6DB5;
    --navy: #15224B;
    --arrow: #B9BBBE;
    --ink: #1E1E1E;
    --white: #FFFFFF;
    --ring-edge: #E2E4E8;
  }
  html, body { margin: 0; padding: 0; width: 1200px; height: 1200px; overflow: hidden; background: var(--white); }
  .diagram { display: block; width: 1200px; height: 1200px; font-family: "Roboto", Arial, sans-serif; }
  .quadrant-financial { fill: var(--orange); }
  .quadrant-operational { fill: var(--sky); }
  .quadrant-organizational { fill: var(--royal); }
  .quadrant-strategic { fill: var(--navy); }
  .band { fill: none; stroke-width: 15; }
  .band-financial { stroke: var(--orange); }
  .band-operational { stroke: var(--sky); }
  .band-organizational { stroke: var(--royal); }
  .band-strategic { stroke: var(--navy); }
  .divider { stroke: var(--white); stroke-width: 9; }
  .hub { fill: var(--white); stroke: var(--ring-edge); stroke-width: 6; }
  .hub-title { fill: var(--navy); font-weight: 700; font-size: 34px; text-anchor: middle; }
  .quadrant-label { fill: var(--white); font-weight: 500; font-size: 44px; }
  .node { stroke: var(--white); stroke-width: 4; }
  .node-financial { fill: var(--orange); }
  .node-strategic { fill: var(--navy); }
  .connector { stroke: var(--arrow); stroke-width: 3.5; fill: none; }
  .arrow-head { fill: var(--arrow); }
  .bubble-fill { fill: var(--white); }
  .bubble-base { fill: none; stroke: var(--sky); stroke-width: 4; }
  .bubble-accent-financial { fill: none; stroke: var(--orange); stroke-width: 4; stroke-dasharray: 172.8 400; }
  .bubble-accent-strategic { fill: none; stroke: var(--navy); stroke-width: 4; stroke-dasharray: 172.8 400; }
  .bubble-text { fill: var(--ink); font-size: 15.5px; text-anchor: middle; }
</style>
</head>
<body>
<svg class="diagram" viewBox="0 0 1080 1080" xmlns="http://www.w3.org/2000/svg" role="img" aria-label="Types of Corporate Restructuring diagram">
  <defs>
    <marker id="arrowhead" viewBox="0 0 10 10" refX="6" refY="5" markerWidth="4" markerHeight="4" orient="auto">
      <path class="arrow-head" d="M0,0 L10,5 L0,10 Z"/>
    </marker>
    <path id="path-financial" d="M355,545 A190,190 0 0 1 545,355"/>
    <path id="path-operational" d="M545,355 A190,190 0 0 1 735,545"/>
    <path id="path-organizational" d="M545,772 A227,227 0 0 0 772,545"/>
    <path id="path-strategic" d="M318,545 A227,227 0 0 0 545,772"/>
  </defs>

  <!-- outer band -->
  <path class="band band-financial" d="M275,545 A270,270 0 0 1 545,275"/>
  <path class="band band-operational" d="M545,275 A270,270 0 0 1 815,545"/>
  <path class="band band-organizational" d="M815,545 A270,270 0 0 1 545,815"/>
  <path class="band band-strategic" d="M545,815 A270,270 0 0 1 275,545"/>

  <!-- quadrants -->
  <path class="quadrant-financial" d="M545,545 L300,545 A245,245 0 0 1 545,300 Z"/>
  <path class="quadrant-operational" d="M545,545 L545,300 A245,245 0 0 1 790,545 Z"/>
  <path class="quadrant-organizational" d="M545,545 L790,545 A245,245 0 0 1 545,790 Z"/>
  <path class="quadrant-strategic" d="M545,545 L545,790 A245,245 0 0 1 300,545 Z"/>
  <line class="divider" x1="290" y1="545" x2="800" y2="545"/>
  <line class="divider" x1="545" y1="290" x2="545" y2="800"/>

  <!-- quadrant labels -->
  <text class="quadrant-label"><textPath href="#path-financial" startOffset="50%" text-anchor="middle">Financial</textPath></text>
  <text class="quadrant-label"><textPath href="#path-operational" startOffset="50%" text-anchor="middle">Operational</textPath></text>
  <text class="quadrant-label"><textPath href="#path-organizational" startOffset="50%" text-anchor="middle">Organizational</textPath></text>
  <text class="quadrant-label"><textPath href="#path-strategic" startOffset="50%" text-anchor="middle">Strategic</textPath></text>

  <!-- hub -->
  <circle class="hub" cx="545" cy="545" r="162"/>
  <text class="hub-title" x="545" y="510">Types of</text>
  <text class="hub-title" x="545" y="548">Corporate</text>
  <text class="hub-title" x="545" y="586">Restructuring</text>

  <!-- connectors -->
  <g marker-end="url(#arrowhead)">
    <line class="connector" x1="510" y1="256" x2="499" y2="208"/>
    <line class="connector" x1="420" y1="282" x2="406" y2="238"/>
    <line class="connector" x1="346" y1="334" x2="312" y2="296"/>
    <line class="connector" x1="290" y1="406" x2="250" y2="384"/>
    <line class="connector" x1="266" y1="492" x2="212" y2="487"/>
    <line class="connector" x1="270" y1="620" x2="214" y2="629"/>
    <line class="connector" x1="314" y1="708" x2="274" y2="727"/>
    <line class="connector" x1="384" y1="778" x2="352" y2="818"/>
    <line class="connector" x1="477" y1="820" x2="464" y2="864"/>
  </g>

  <!-- nodes -->
  <circle class="node node-financial" cx="514" cy="274" r="13"/>
  <circle class="node node-financial" cx="426" cy="298" r="13"/>
  <circle class="node node-financial" cx="358" cy="348" r="13"/>
  <circle class="node node-financial" cx="305" cy="420" r="13"/>
  <circle class="node node-financial" cx="282" cy="494" r="13"/>
  <circle class="node node-strategic" cx="287" cy="616" r="13"/>
  <circle class="node node-strategic" cx="328" cy="699" r="13"/>
  <circle class="node node-strategic" cx="396" cy="766" r="13"/>
  <circle class="node node-strategic" cx="482" cy="802" r="13"/>

  <!-- financial bubbles -->
  <g class="bubble" transform="translate(487,142)">
    <circle class="bubble-fill bubble-base" r="55"/>
    <circle class="bubble-accent-financial" r="55" transform="rotate(-135)"/>
    <text class="bubble-text" y="-5">Covenant</text>
    <text class="bubble-text" y="15">Breach(es)</text>
  </g>
  <g class="bubble" transform="translate(370,176)">
    <circle class="bubble-fill bubble-base" r="55"/>
    <circle class="bubble-accent-financial" r="55" transform="rotate(-135)"/>
    <text class="bubble-text" y="-5">Creditor</text>
    <text class="bubble-text" y="15">Pressure</text>
  </g>
  <g class="bubble" transform="translate(267,243)">
    <circle class="bubble-fill bubble-base" r="55"/>
    <circle class="bubble-accent-financial" r="55" transform="rotate(-135)"/>
    <text class="bubble-text" y="-15">Creditors</text>
    <text class="bubble-text" y="5">in control</text>
    <text class="bubble-text" y="25">of strategy</text>
  </g>
  <g class="bubble" transform="translate(190,347)">
    <circle class="bubble-fill bubble-base" r="55"/>
    <circle class="bubble-accent-financial" r="55" transform="rotate(-135)"/>
    <text class="bubble-text" y="-5">Expensive</text>
    <text class="bubble-text" y="15">Re-financing</text>
  </g>
  <g class="bubble" transform="translate(148,462)">
    <circle class="bubble-fill bubble-base" r="55"/>
    <circle class="bubble-accent-financial" r="55" transform="rotate(-135)"/>
    <text class="bubble-text" y="-15">Equity</text>
    <text class="bubble-text" y="5">Values</text>
    <text class="bubble-text" y="25">Negligible</text>
  </g>

  <!-- strategic bubbles -->
  <g class="bubble" transform="translate(148,627)">
    <circle class="bubble-fill bubble-base" r="55"/>
    <circle class="bubble-accent-strategic" r="55" transform="rotate(-135)"/>
    <text class="bubble-text" y="-15">Potential</text>
    <text class="bubble-text" y="5">Covenant</text>
    <text class="bubble-text" y="25">Breach</text>
  </g>
  <g class="bubble" transform="translate(205,765)">
    <circle class="bubble-fill bubble-base" r="55"/>
    <circle class="bubble-accent-strategic" r="55" transform="rotate(-135)"/>
    <text class="bubble-text" y="-15">Credit</text>
    <text class="bubble-text" y="5">Rating</text>
    <text class="bubble-text" y="25">Downgrade</text>
  </g>
  <g class="bubble" transform="translate(308,878)">
    <circle class="bubble-fill bubble-base" r="55"/>
    <circle class="bubble-accent-strategic" r="55" transform="rotate(-135)"/>
    <text class="bubble-text" y="-5">Profit</text>
    <text class="bubble-text" y="15">Warning</text>
  </g>
  <g class="bubble" transform="translate(444,938)">
    <circle class="bubble-fill bubble-base" r="55"/>
    <circle class="bubble-accent-strategic" r="55" transform="rotate(-135)"/>
    <text class="bubble-text" y="-15">Board Still</text>
    <text class="bubble-text" y="5">in Control of</text>
    <text class="bubble-text" y="25">Strategy</text>
  </g>
</svg>
</body>
</html>
```